Real estate broker business card

Want a modern celan but effective business card for my residential and commercial real estate business. I want the back of the card to advertise my services and to capture business. I have attached the back of my current business card fore ideas
Updates

Target Market(s)

home buyers and seller. commercial buyers and sellers

Industry/Entity Type

Real Estate

Contact Information for Business Card

must have my contact information and my photo

Requirements
Must have
• Lorna Vettridge
• Owner & Qualifying Broker
• Brockhill Real Estate Services
• 555.218.7094
• lorna@brockhillhomes.example
• www.brockhillhomes.example
Nice to have
• metallic
• Business capture text: " Don't buy or lease property without someone looking out for your best interests. I will represent you on your home or investment purchase for FREE!"
• "Home owners, call today to receive a FREE market analysis for your homes value!

```html
<!DOCTYPE html>
<html lang="en">
<head>
<meta charset="utf-8">
<title>Brockhill Real Estate Services – Business Card</title>
<link rel="stylesheet" href="https://fonts.googleapis.com/css2?family=Cinzel:wght@600;700&family=Montserrat:wght@400;500;600&display=swap">
<style>
  :root {
    --stage: #2e2f31;
    --card-back: #e4e5e7;
    --card-front: #ffffff;
    --teal: #1d7682;
    --teal-dark: #155a63;
    --ink: #4a4c4f;
    --ink-soft: #5d6064;
    --photo-a: #3f5a3a;
    --photo-b: #7a6a5e;
    --frame: #5a5a5a;
  }
  * { box-sizing: border-box; margin: 0; padding: 0; }
  html, body { width: 1200px; height: 900px; overflow: hidden; }
  body {
    background: var(--stage);
    font-family: "Montserrat", sans-serif;
    color: var(--ink);
    display: flex;
    flex-direction: column;
    align-items: center;
    justify-content: center;
    gap: 36px;
  }
  .card {
    width: 700px;
    height: 400px;
    border-radius: 26px;
    position: relative;
    overflow: hidden;
    box-shadow: 0 10px 28px rgba(0,0,0,.45);
  }
  .card--back { background: var(--card-back); }
  .card--front { background: var(--card-front); }

  .brand {
    display: flex;
    align-items: center;
    gap: 14px;
    position: absolute;
  }
  .brand__dot {
    width: 54px; height: 54px;
    border-radius: 50%;
    background: var(--teal);
    flex: none;
  }
  .brand__name {
    font-family: "Cinzel", serif;
    font-weight: 700;
    color: var(--teal);
    line-height: 1.05;
  }
  .brand__name .brand__line1 { display: block; font-size: 44px; letter-spacing: 1px; }
  .brand__name .brand__line2 { display: block; font-size: 15.5px; letter-spacing: 2.4px; }

  .card--back .brand { left: 170px; top: 86px; }

  .pitch {
    position: absolute;
    left: 62px;
    top: 218px;
    width: 520px;
    font-size: 16px;
    line-height: 1.32;
    color: var(--ink-soft);
  }
  .pitch p + p { margin-top: 10px; }
  .pitch .free { color: var(--teal); font-weight: 600; }

  .card--front .brand { left: 40px; top: 118px; }
  .card--front .brand__dot { width: 48px; height: 48px; }
  .card--front .brand__name .brand__line1 { font-size: 38px; }
  .card--front .brand__name .brand__line2 { font-size: 13.4px; letter-spacing: 2.1px; }

  .portrait {
    position: absolute;
    left: 418px;
    top: 34px;
    width: 232px;
    height: 186px;
    border: 4px solid var(--frame);
    background: linear-gradient(120deg, var(--photo-a) 0%, var(--photo-a) 40%, var(--photo-b) 70%, #d9d4cd 100%);
  }
  .contact {
    position: absolute;
    left: 430px;
    top: 238px;
  }
  .contact__name {
    font-family: "Cinzel", serif;
    font-weight: 700;
    font-size: 25px;
    color: var(--teal);
    letter-spacing: .5px;
  }
  .contact__title {
    font-size: 14.5px;
    color: var(--ink-soft);
    margin-top: 2px;
  }
  .contact__list {
    list-style: none;
    margin-top: 14px;
  }
  .contact__list li {
    display: flex;
    align-items: center;
    gap: 12px;
    font-size: 15px;
    color: var(--ink);
    line-height: 1.6;
  }
  .contact__list svg { width: 13px; height: 13px; flex: none; }
</style>
</head>
<body>

<section class="card card--back" aria-label="Card back">
  <div class="brand">
    <span class="brand__dot"></span>
    <span class="brand__name"><span class="brand__line1">BROCKHILL</span><span class="brand__line2">REAL ESTATE SERVICES</span></span>
  </div>
  <div class="pitch">
    <p>Don't buy or lease property without<br>someone looking out for your best interests.<br>I will represent you on your home<br>or investment purchase for <span class="free">FREE</span>!</p>
    <p>Home owners, call today to receive a<br><span class="free">FREE</span> market analysis for your homes value!</p>
  </div>
</section>

<section class="card card--front" aria-label="Card front">
  <div class="brand">
    <span class="brand__dot"></span>
    <span class="brand__name"><span class="brand__line1">BROCKHILL</span><span class="brand__line2">REAL ESTATE SERVICES</span></span>
  </div>

  <div class="portrait" role="img" aria-label="Portrait photo of Lorna Vettridge"></div>

  <div class="contact">
    <h1 class="contact__name">LORNA VETTRIDGE</h1>
    <p class="contact__title">Owner &amp; Qualifying Broker</p>
    <ul class="contact__list">
      <li>
        <svg viewBox="0 0 16 16" aria-hidden="true"><path fill="var(--teal-dark)" d="M3.6 1.2 6 3.6 4.7 5.6c.8 1.9 2.4 3.5 4.3 4.3l2-1.3 2.4 2.4-1.6 2.2C7 13 2.6 8.6 1.4 3z"/></svg>
        555.218.7094
      </li>
      <li>
        <svg viewBox="0 0 16 16" aria-hidden="true"><rect x="1.5" y="3.5" width="13" height="9" fill="none" stroke="var(--teal-dark)" stroke-width="1.6"/><path d="M1.5 3.5 8 9l6.5-5.5" fill="none" stroke="var(--teal-dark)" stroke-width="1.6"/></svg>
        lorna@brockhillhomes.example
      </li>
      <li>
        <svg viewBox="0 0 16 16" aria-hidden="true"><circle cx="8" cy="8" r="6.4" fill="none" stroke="var(--teal-dark)" stroke-width="1.4"/><ellipse cx="8" cy="8" rx="2.8" ry="6.4" fill="none" stroke="var(--teal-dark)" stroke-width="1.2"/><path d="M1.6 8h12.8" stroke="var(--teal-dark)" stroke-width="1.2"/></svg>
        www.brockhillhomes.example
      </li>
    </ul>
  </div>
</section>

</body>
</html>
```